Velmora Biz Card 2019

New business card for Velmora Property Inspections. We are a residential home inspection company in Arizona.

Target Market(s)

Real Estate

Font styles to use
Sans Serif

Requirements
Must have
• Glen Mirewick
• Home Inspector
• Velmora Property Inspections, LLC
• 480-555-0172
• glen@velmora-llc.example

```html
<!DOCTYPE html>
<html lang="en">
<head>
<meta charset="utf-8">
<title>Velmora Biz Card 2019</title>
<link rel="stylesheet" href="https://fonts.googleapis.com/css2?family=Montserrat:wght@700&family=Tinos:wght@400;700&display=swap">
<style>
  :root {
    --backdrop: #e6e7e9;
    --card: #2a292b;
    --green: #4db848;
    --ink-line: #141414;
    --logo-text: #ececec;
    --icon: #c9ced1;
  }
  * { margin: 0; padding: 0; box-sizing: border-box; }
  html, body {
    width: 1200px; height: 1200px; overflow: hidden;
    background: var(--backdrop);
  }
  .canvas { position: relative; width: 1200px; height: 1200px; }
  .card {
    position: absolute; left: 211px; width: 800px; height: 456px;
    background: var(--card); overflow: hidden;
  }
  .card--front { top: 142px; }
  .card--back { top: 626px; }

  .top-bar {
    position: absolute; left: 190px; top: 0; width: 430px; height: 38px;
    background: var(--green);
    box-shadow: 0 6px 10px rgba(0,0,0,0.45);
  }
  .corner-slash { position: absolute; inset: 0; width: 800px; height: 456px; }

  .brand-name {
    position: absolute; left: 0; width: 800px; top: 172px;
    text-align: center;
    font-family: "Montserrat", sans-serif; font-weight: 700;
    font-size: 46px; letter-spacing: 1px; text-transform: uppercase;
    color: var(--logo-text);
  }

  .side-tab {
    position: absolute; top: 86px; height: 334px; background: var(--green);
    box-shadow: 0 6px 12px rgba(0,0,0,0.45);
  }
  .side-tab--left { left: 0; width: 50px; border-radius: 0 18px 18px 0; }
  .side-tab--right { left: 754px; width: 46px; border-radius: 18px 0 0 18px; }

  .person-name {
    position: absolute; left: 0; width: 800px; top: 118px;
    text-align: center;
    font-family: "Tinos", "Times New Roman", serif; font-weight: 700;
    font-size: 83px; line-height: 1; color: var(--green);
  }
  .details { position: absolute; left: 171px; top: 232px; list-style: none; }
  .details li {
    display: flex; align-items: center; height: 45px;
    font-family: "Tinos", "Times New Roman", serif; font-size: 28px;
    color: var(--green);
  }
  .details svg { width: 42px; height: 34px; margin-right: 14px; flex: none; }
</style>
</head>
<body>
<div class="canvas">

  <section class="card card--front">
    <div class="top-bar"></div>
    <svg class="corner-slash" viewBox="0 0 800 456" aria-hidden="true">
      <polygon points="800,138 800,174 475,456 435,456" fill="var(--green)"/>
      <polygon points="800,158 800,166 468,456 456,456" fill="var(--ink-line)"/>
      <polygon points="800,174 800,456 475,456" fill="var(--green)"/>
    </svg>
    <div class="brand-name">Velmora</div>
  </section>

  <section class="card card--back">
    <div class="side-tab side-tab--left"></div>
    <div class="side-tab side-tab--right"></div>
    <h1 class="person-name">Glen Mirewick</h1>
    <ul class="details">
      <li>
        <svg viewBox="0 0 42 34" aria-hidden="true">
          <polygon points="21,2 4,14 38,14" fill="var(--icon)"/>
          <rect x="7" y="15" width="28" height="17" fill="var(--icon)"/>
          <rect x="17" y="21" width="8" height="11" fill="var(--card)"/>
        </svg>
        Home Inspector
      </li>
      <li>
        <svg viewBox="0 0 42 34" aria-hidden="true">
          <polygon points="29,4 21,10 37,10" fill="var(--icon)"/>
          <rect x="23" y="10" width="12" height="9" fill="var(--icon)"/>
          <rect x="1" y="20" width="6" height="10" fill="var(--icon)"/>
          <path d="M8 21 h10 q4 0 6 2 h12 q4 0 3 3 l-10 5 h-21 z" fill="var(--icon)"/>
        </svg>
        Velmora Property Inspections, LLC
      </li>
      <li>
        <svg viewBox="0 0 42 34" aria-hidden="true">
          <path d="M9 4 l6 -1 l3 8 l-4 3 q2 6 8 10 l3 -4 l8 3 l-1 6 q-14 2 -23 -25 z" fill="none" stroke="var(--icon)" stroke-width="2.5" stroke-linejoin="round"/>
          <path d="M24 6 q6 1 7 7 M25 1 q10 1 11 12" fill="none" stroke="var(--icon)" stroke-width="2"/>
        </svg>
        480-555-0172
      </li>
      <li>
        <svg viewBox="0 0 42 34" aria-hidden="true">
          <rect x="2" y="4" width="38" height="27" rx="2" fill="none" stroke="var(--icon)" stroke-width="3"/>
          <path d="M3 6 l18 15 l18 -15" fill="none" stroke="var(--icon)" stroke-width="3"/>
        </svg>
        glen@velmora-llc.example
      </li>
    </ul>
  </section>

</div>
</body>
</html>
```